Brochure Design for Professional Car Detailing Service

Existing car wash business running under new management requires a brochure with catchy phrases and eye grabbing designs to make clients aware of new management and special deals. Images used are to be royalty free as business cannot supply all images, company logo to be supplied to winner -- please use test logo provided for now.

This is for the graphic and advertising/marketing guru minded -- this brochure will only be the start of many marketing/advertising promotions running for our business in the next few months to come to introduce deals and specials under new management, and one of many continuos future advertising promotions.

Please apply only if you are interested and can supply quality work, as we are a professional business.

We have never used this service before hence no guarantee that a winner will be chosen -- as we have been burnt in the past with other freelancer sites, where we have had a similar contest with poor quality work and were forced to pay for nonsense. We will be more then happy to pay for quality work.

Looking forward to working with you.

- Management

The brochure will be professional, though eye catching and fresh -- attracting a wide range of cliental i.e. professionals, young car owners, mums and dads, etc.

Brochure will include:

contact details and address on bottom of each page -- small but noticeable

** A front page that yells out under new management and a quick peak at managers specials available on selected detailing services <= you word it with your marketing experience
** inner left page discusses 'about us' <== make this up, we'll send the proper wording to the winner for finale changes. Also this page should include a map on where to find us and contact details in bigger writing/more detail.
** inner middle pane to be price list of all detail services available
** inner right page -- details managers specials available
**Back page to be coupons that can be cut out with managers specials.

```html
<!DOCTYPE html>
<html lang="en">
<head>
<meta charset="utf-8">
<title>Pro Detailing Services – Brochure Cover</title>
<link rel="stylesheet" href="https://fonts.googleapis.com/css2?family=Montserrat:wght@600;700;800&family=Open+Sans:wght@400;600&family=Jost:wght@500;600;700&display=swap">
<style>
  :root {
    --panel-left: #f9b05c;
    --panel-middle: #f7a42a;
    --panel-right: #fcb648;
    --accent-band: #f59a1c;
    --photo-light: #f6c34a;
    --photo-mid: #d89a25;
    --photo-dark: #8a5a14;
    --ink: #23232f;
    --ink-soft: #3a3340;
    --royal: #1f2cb3;
    --navy: #1c2170;
    --maroon: #8c1c2a;
    --ring-orange: #e07a10;
    --white: #ffffff;
  }
  html, body { margin: 0; padding: 0; overflow: hidden; background: #ffffff; }
  .brochure {
    position: relative;
    width: 1200px;
    height: 853px;
    overflow: hidden;
    background: var(--panel-middle);
    font-family: "Open Sans", Arial, sans-serif;
    color: var(--ink);
  }
  .backdrop { position: absolute; inset: 0; }

  /* Left panel – coupons */
  .coupon-panel { position: absolute; left: 0; top: 0; width: 400px; height: 853px; }
  .coupon-panel__title {
    position: absolute; left: 46px; top: 350px; margin: 0;
    font-family: "Montserrat", Arial, sans-serif;
    line-height: 1;
  }
  .coupon-panel__kicker {
    display: block; font-size: 36px; font-weight: 700; letter-spacing: 3.4px; color: var(--ink-soft);
  }
  .coupon-panel__headline {
    display: block; margin-top: 6px; font-size: 40px; font-weight: 700; letter-spacing: 0.5px; color: var(--royal);
  }
  .coupon-panel__intro {
    position: absolute; left: 46px; top: 438px; width: 320px; margin: 0;
    font-size: 13px; line-height: 15px; color: var(--ink-soft);
  }
  .coupon { position: absolute; left: 44px; width: 302px; height: 108px; }

  /* Middle panel – contact */
  .contact { position: absolute; left: 400px; top: 572px; width: 394px; text-align: center; color: var(--ink); font-style: normal; }
  .contact__pin { display: block; margin: 0 auto 8px; }
  .contact__office { margin: 0; font-size: 19px; }
  .contact__address { margin: 4px 0 0; font-size: 13px; }
  .contact__phones { margin: 22px 0 0; font-size: 13px; line-height: 18px; }
  .contact__email { margin: 22px 0 0; font-size: 13px; }
  .contact__web { margin: 2px 0 0; font-size: 19px; }
  .contact__social { margin: 6px 0 0; font-size: 15px; color: var(--ink-soft); letter-spacing: 0.3px; }

  /* Right panel – front cover */
  .brand-plate {
    position: absolute; left: 1047px; top: 218px; width: 138px; height: 88px;
    background: #f4efe2; border-radius: 6px;
    display: flex; align-items: center; justify-content: center; gap: 8px;
    box-shadow: inset 0 0 0 2px #d7c9a6;
  }
  .brand-plate__dot { width: 12px; height: 12px; border-radius: 50%; background: var(--navy); }
  .brand-plate__name { font-family: "Jost", Arial, sans-serif; font-weight: 600; font-size: 30px; color: var(--navy); }

  .guarantee { position: absolute; right: 22px; top: 458px; width: 116px; text-align: center; }
  .guarantee__seal { display: block; margin: 0 auto 6px; }
  .guarantee__text {
    margin: 0; font-family: "Jost", Arial, sans-serif; font-weight: 500;
    font-size: 14px; line-height: 17px; color: var(--ink);
  }
  .guarantee__text strong { font-weight: 700; }

  .service-title {
    position: absolute; left: 820px; top: 570px; margin: 0;
    font-family: "Jost", Arial, sans-serif; font-weight: 600;
    font-size: 46px; line-height: 40px; color: var(--ink); letter-spacing: -1px;
    white-space: nowrap;
  }
  .service-title__line { display: block; }
  .service-title__accent { color: var(--maroon); }
  .service-title__ic { color: var(--royal); }
  .tagline {
    position: absolute; left: 1024px; top: 658px; margin: 0;
    font-family: "Jost", Arial, sans-serif; font-weight: 500;
    font-size: 17px; line-height: 16px; color: var(--royal);
    white-space: nowrap;
  }
  .announcement {
    position: absolute; left: 884px; top: 722px; width: 232px; margin: 0; text-align: center;
    font-family: "Jost", Arial, sans-serif; font-weight: 600;
    font-size: 33px; line-height: 30px; color: var(--ink); white-space: nowrap;
  }
  .announcement__new { color: var(--royal); font-weight: 500; position: relative; top: -6px; }
  .specials-cue {
    position: absolute; right: 24px; top: 782px; margin: 0; text-align: right;
    font-family: "Jost", Arial, sans-serif; font-weight: 700; color: var(--navy);
  }
  .specials-cue__for { display: block; font-size: 12px; line-height: 12px; color: var(--ink); padding-right: 4px; }
  .specials-cue__main { display: block; font-size: 20px; line-height: 20px; }
  .specials-cue__sub { display: block; font-size: 16px; line-height: 18px; color: var(--ink); font-weight: 600; }
</style>
</head>
<body>
<main class="brochure">

  <svg class="backdrop" width="1200" height="853" viewBox="0 0 1200 853">
    <defs>
      <linearGradient id="car-tones" x1="0" y1="0" x2="1" y2="1">
        <stop offset="0" stop-color="#f6c34a"/>
        <stop offset="0.45" stop-color="#d89a25"/>
        <stop offset="0.8" stop-color="#f6c34a"/>
        <stop offset="1" stop-color="#8a5a14"/>
      </linearGradient>
    </defs>
    <rect class="panel-left" x="0" y="0" width="400" height="853" fill="var(--panel-left)"/>
    <rect class="panel-middle" x="400" y="0" width="395" height="853" fill="var(--panel-middle)"/>
    <polygon class="panel-right" points="795,500 1200,420 1200,853 795,853" fill="var(--panel-right)"/>
    <polygon class="accent-band" points="740,448 1200,356 1200,530 795,505" fill="var(--accent-band)"/>
    <polygon class="hero-photo" role="img" aria-label="Photograph of a gold-toned hatchback car, front three-quarter view"
             points="0,0 1200,0 1200,356 740,448 400,313 0,330" fill="url(#car-tones)"/>
    <g class="rings" fill="none">
      <circle cx="815" cy="560" r="13" stroke="var(--ring-orange)" stroke-width="2"/>
      <circle cx="925" cy="577" r="6" stroke="var(--ink-soft)" stroke-width="1.5"/>
      <circle cx="845" cy="743" r="17" stroke="var(--ring-orange)" stroke-width="2"/>
      <circle cx="803" cy="827" r="48" stroke="var(--royal)" stroke-width="3"/>
      <circle cx="903" cy="807" r="25" stroke="var(--maroon)" stroke-width="3"/>
      <circle cx="925" cy="775" r="6" stroke="var(--ink-soft)" stroke-width="1.5"/>
    </g>
  </svg>

  <div class="brand-plate">
    <span class="brand-plate__dot"></span>
    <span class="brand-plate__name">Velo</span>
  </div>

  <section class="coupon-panel">
    <h2 class="coupon-panel__title">
      <span class="coupon-panel__kicker">PROFESSIONAL</span>
      <span class="coupon-panel__headline">BUSINESS TEXT</span>
    </h2>
    <p class="coupon-panel__intro">Wandis samadse edane kaharm kalalate fuga eats quisquaerum ium quiatem voluptium laut alitiust res nem quam, cuse utoccu made</p>

    <svg class="coupon" style="top:500px" width="302" height="108" viewBox="0 0 302 108">
      <rect x="1.5" y="1.5" width="299" height="105" rx="12" fill="none" stroke="var(--royal)" stroke-width="2" stroke-dasharray="7 5"/>
      <g class="scissors" stroke="var(--royal)" stroke-width="1.6" fill="none">
        <circle cx="272" cy="16" r="3.5"/><circle cx="281" cy="16" r="3.5"/>
        <line x1="273" y1="19" x2="282" y2="31"/><line x1="280" y1="19" x2="271" y2="31"/>
      </g>
    </svg>
    <svg class="coupon" style="top:672px" width="302" height="108" viewBox="0 0 302 108">
      <rect x="1.5" y="1.5" width="299" height="105" rx="12" fill="none" stroke="var(--royal)" stroke-width="2" stroke-dasharray="7 5"/>
      <g class="scissors" stroke="var(--royal)" stroke-width="1.6" fill="none">
        <circle cx="272" cy="16" r="3.5"/><circle cx="281" cy="16" r="3.5"/>
        <line x1="273" y1="19" x2="282" y2="31"/><line x1="280" y1="19" x2="271" y2="31"/>
      </g>
    </svg>
  </section>

  <address class="contact">
    <svg class="contact__pin" width="18" height="26" viewBox="0 0 18 26">
      <path d="M9 0C4 0 0 4 0 9c0 6.5 9 17 9 17s9-10.5 9-17c0-5-4-9-9-9z" fill="var(--royal)"/>
      <circle cx="9" cy="9" r="3.4" fill="var(--panel-middle)"/>
    </svg>
    <p class="contact__office">Head Office</p>
    <p class="contact__address">A. 412-420 Harbour Lane WESTFIELD</p>
    <p class="contact__phones">TEL: (03) 5550 1482<br>MOB: + 61 400 555 219<br>Call for Support!</p>
    <p class="contact__email">hello@velowestfield.com</p>
    <p class="contact__web">www.velowestfield.com</p>
    <p class="contact__social">Social Ad / Video Ad</p>
  </address>

  <aside class="guarantee">
    <svg class="guarantee__seal" width="46" height="46" viewBox="0 0 46 46">
      <circle cx="23" cy="23" r="22" fill="var(--navy)"/>
      <circle cx="23" cy="23" r="16" fill="#f2c230"/>
    </svg>
    <p class="guarantee__text">We offer a <strong>100%</strong><br><strong>No Scratch<br>Guarantee<br>Find out more.</strong></p>
  </aside>

  <h1 class="service-title">
    <span class="service-title__line">PR<span class="service-title__accent">O</span></span>
    <span class="service-title__line">DETAILING</span>
    <span class="service-title__line">SERV<span class="service-title__ic">iC</span>ES</span>
  </h1>
  <p class="tagline">Where every<br>little detail counts</p>

  <p class="announcement">“Under <span class="announcement__new">NEW</span><br>Management”</p>

  <p class="specials-cue">
    <span class="specials-cue__for">FOR</span>
    <span class="specials-cue__main">SPECIALS</span>
    <span class="specials-cue__sub">See inside...</span>
  </p>

</main>
</body>
</html>
```